QN Flier and Logo

We need a one-page color marketing consumer flier and a new logo.

Target Market(s)

Seniors

Font styles to use
Sans Serif

Colors
85acd3

Requirements
Must have
• Veteran or Military theme, Benefit amounts.

```html
<!DOCTYPE html>
<html lang="en">
<head>
<meta charset="utf-8">
<title>QN Veterans Benefits Flier</title>
<link href="https://fonts.googleapis.com/css2?family=Montserrat:wght@300;400;500;600;700;800&family=Oswald:wght@400;500&display=swap" rel="stylesheet">
<style>
  :root {
    --navy: #1c2470;
    --red: #e8202a;
    --sky: #85acd3;
    --sky-dark: #7ea6cf;
    --panel: #e9e9ec;
    --paper: #ffffff;
    --backdrop: #3c3d40;
    --hero-deep: #0f1a6e;
    --hero-mid: #27339a;
  }
  * { margin: 0; padding: 0; box-sizing: border-box; }
  html, body { width: 1200px; height: 1200px; overflow: hidden; }
  body { background: var(--backdrop); font-family: "Montserrat", sans-serif; color: var(--navy); position: relative; }

  .flier {
    position: absolute; left: 191px; top: 20px;
    width: 838px; height: 1190px;
    transform: scale(0.975); transform-origin: top left;
    background: linear-gradient(180deg, var(--paper) 60%, #ececee 88%, var(--paper) 100%);
    overflow: hidden;
  }
  .abs { position: absolute; }

  .hero { left: 0; top: 0; width: 838px; height: 437px; }
  .hero-photo {
    position: absolute; inset: 0;
    background:
      radial-gradient(ellipse at 75% 10%, rgba(150,70,160,.75), transparent 45%),
      radial-gradient(ellipse at 20% 30%, rgba(60,80,190,.6), transparent 55%),
      linear-gradient(160deg, var(--hero-mid) 0%, var(--hero-deep) 55%, #1a2788 100%);
  }
  .title-top {
    left: 70px; top: 100px; width: 700px;
    font-weight: 800; font-size: 124px; letter-spacing: -2px; line-height: 1;
    color: #fff;
  }
  .title-bottom {
    left: 72px; top: 218px; width: 700px;
    font-weight: 400; font-size: 134px; letter-spacing: 0; line-height: 1;
    color: var(--red);
  }
  .tagline {
    left: 139px; top: 375px; width: 561px; height: 62px;
    background: var(--red); border-radius: 12px 12px 0 0;
    color: #fff; font-weight: 700; font-size: 15.5px; line-height: 21px;
    text-align: center; padding-top: 11px;
  }

  .cta-bar {
    left: 69px; top: 451px; width: 700px; height: 32px;
    background: var(--sky); border-bottom: 2px solid #6f95c0;
    text-align: center; font-weight: 700; font-size: 17px; line-height: 32px; letter-spacing: .5px;
  }
  .rates {
    left: 69px; top: 483px; width: 700px; height: 162px; background: var(--panel);
  }
  .rates .divider { left: 347px; top: 24px; width: 1px; height: 116px; background: #b9bccc; }
  .rate { position: absolute; }
  .rate-name { font-weight: 700; font-size: 16px; letter-spacing: .4px; line-height: 1; }
  .rate-note { font-weight: 400; font-size: 11.5px; letter-spacing: .3px; line-height: 1; margin-top: 1px; }
  .rate-amount { display: flex; align-items: baseline; margin-top: 7px; color: var(--red); }
  .rate-amount .upto { font-family: "Oswald", sans-serif; font-size: 12px; color: var(--navy); margin-right: 4px; }
  .rate-amount .cur { font-family: "Oswald", sans-serif; font-size: 10px; align-self: flex-start; margin-right: 2px; }
  .rate-amount .num { font-family: "Oswald", sans-serif; font-size: 22px; line-height: 1; }
  .rate-amount .per { font-weight: 800; font-size: 19px; margin-left: 6px; letter-spacing: .3px; }

  .section-head { font-weight: 700; font-size: 17px; letter-spacing: .4px; }
  .eligibility { left: 64px; top: 686px; width: 380px; }
  .checklist { list-style: none; margin-top: 14px; }
  .checklist li {
    position: relative; padding-left: 30px;
    font-size: 14.5px; line-height: 18px; margin-bottom: 15px; font-weight: 400;
  }
  .checklist svg { position: absolute; left: 6px; top: 3px; }
  .col-divider { left: 470px; top: 688px; width: 1px; height: 308px; background: #c6c8d2; }

  .criteria { left: 531px; width: 240px; }
  .criteria h3 { color: var(--red); font-weight: 700; font-size: 17px; letter-spacing: .5px; margin-bottom: 6px; }
  .criteria p { font-size: 11.2px; line-height: 14.5px; text-align: justify; }

  .footer { left: 0; top: 1043px; width: 838px; height: 77px; background: var(--sky-dark); }
  .footer .sep { top: 9px; width: 1px; height: 59px; background: #a8c3e0; }
  .advisor { left: 70px; top: 16px; font-weight: 700; font-size: 13.5px; letter-spacing: .3px; }
  .phone { left: 70px; top: 36px; display: flex; align-items: center; gap: 8px; font-weight: 700; font-size: 20px; }
  .address { left: 365px; top: 16px; display: flex; gap: 8px; font-size: 12.5px; line-height: 15.5px; }
  .contact-extra { left: 645px; top: 23px; width: 170px; font-size: 12.5px; line-height: 20px; white-space: nowrap; }
  .contact-extra .web { display: flex; align-items: center; gap: 6px; margin-left: -4px; font-size: 11.5px; }

  .disclaimer { left: 70px; top: 1135px; width: 700px; text-align: center; font-size: 10.5px; line-height: 14px; }
</style>
</head>
<body>
  <main class="flier">
    <header class="hero abs">
      <div class="hero-photo" role="img" aria-label="American flag waving over a desk with a laptop and financial charts, tinted deep blue"></div>
      <h1>
        <span class="title-top abs">VETERANS</span>
        <span class="title-bottom abs">BENEFITS</span>
      </h1>
      <p class="tagline abs">This benefit can provide a significant monthly income to those<br>who meet the eligibility requirements.</p>
    </header>

    <div class="cta-bar abs">CALL TO SET UP AN APPOINTMENT TODAY!</div>

    <section class="rates abs">
      <div class="divider abs"></div>
      <div class="rate" style="left:27px;top:25px;">
        <div class="rate-name">MARRIED VETERAN</div>
        <div class="rate-note">WITH CARE NEEDS</div>
        <div class="rate-amount"><span class="upto">UP TO</span><span class="cur">$</span><span class="num">2,230</span><span class="per">/ MONTH</span></div>
      </div>
      <div class="rate" style="left:27px;top:114px;">
        <div class="rate-name">SINGLE VETERAN</div>
        <div class="rate-amount"><span class="upto">UP TO</span><span class="cur">$</span><span class="num">1,881</span><span class="per">/ MONTH</span></div>
      </div>
      <div class="rate" style="left:458px;top:27px;">
        <div class="rate-name">SURVIVING SPOUSE</div>
        <div class="rate-amount"><span class="upto">UP TO</span><span class="cur">$</span><span class="num">1,209</span><span class="per">/ MONTH</span></div>
      </div>
      <div class="rate" style="left:458px;top:101px;">
        <div class="rate-name">MARRIED VETERAN</div>
        <div class="rate-note">ONLY SPOUSE NEEDS CARE:</div>
        <div class="rate-amount"><span class="upto">UP TO</span><span class="cur">$</span><span class="num">1,442</span><span class="per">/ MONTH</span></div>
      </div>
    </section>

    <section class="eligibility abs">
      <h2 class="section-head">ELIGIBILITY REQUIREMENTS SERVICE</h2>
      <ul class="checklist">
        <li><svg width="13" height="12" viewBox="0 0 13 12"><path d="M1 6.5 L4.5 10 L12 1.5" fill="none" stroke="#e8202a" stroke-width="2.4"/></svg>World War I</li>
        <li><svg width="13" height="12" viewBox="0 0 13 12"><path d="M1 6.5 L4.5 10 L12 1.5" fill="none" stroke="#e8202a" stroke-width="2.4"/></svg>World War II</li>
        <li><svg width="13" height="12" viewBox="0 0 13 12"><path d="M1 6.5 L4.5 10 L12 1.5" fill="none" stroke="#e8202a" stroke-width="2.4"/></svg>Korean Conflict</li>
        <li><svg width="13" height="12" viewBox="0 0 13 12"><path d="M1 6.5 L4.5 10 L12 1.5" fill="none" stroke="#e8202a" stroke-width="2.4"/></svg>Vietnam Era</li>
        <li><svg width="13" height="12" viewBox="0 0 13 12"><path d="M1 6.5 L4.5 10 L12 1.5" fill="none" stroke="#e8202a" stroke-width="2.4"/></svg>Served in the Republic of Vietnam</li>
        <li><svg width="13" height="12" viewBox="0 0 13 12"><path d="M1 6.5 L4.5 10 L12 1.5" fill="none" stroke="#e8202a" stroke-width="2.4"/></svg>Gulf War</li>
        <li><svg width="13" height="12" viewBox="0 0 13 12"><path d="M1 6.5 L4.5 10 L12 1.5" fill="none" stroke="#e8202a" stroke-width="2.4"/></svg>90 days of active duty service, with<br>at least&nbsp; one day during war time.</li>
        <li><svg width="13" height="12" viewBox="0 0 13 12"><path d="M1 6.5 L4.5 10 L12 1.5" fill="none" stroke="#e8202a" stroke-width="2.4"/></svg>Discharge excluding dishonorable</li>
      </ul>
    </section>

    <div class="col-divider abs"></div>

    <section class="criteria abs" style="top:685px;">
      <h3>HEALTH</h3>
      <p>Disabled and unable to work, or 65+ in need of daily assistance.</p>
    </section>
    <section class="criteria abs" style="top:774px;">
      <h3>INCOME</h3>
      <p>Monthly income (after expenses) must be below the maximum benefit limit. Most individuals receiving care on a regular basis meet this qualification.</p>
    </section>
    <section class="criteria abs" style="top:893px;">
      <h3>NET WORTH</h3>
      <p>In 2018, QN implemented a Bright-Line Net Worth limit but with proper planning most can become eligible. To qualify as a “surviving spouse” you had to have been married to the Veteran until his or her death.</p>
    </section>

    <footer class="footer abs">
      <div class="advisor abs">DANIEL MORROW CFP®, CRPC®</div>
      <div class="phone abs">
        <svg width="22" height="22" viewBox="0 0 22 22"><circle cx="11" cy="11" r="11" fill="#e9eef6"/><path d="M7.2 5.5c.6-.3 1.2 0 1.5.6l1 2c.3.6.1 1.1-.4 1.5l-.6.5c.6 1.4 1.6 2.5 3 3.2l.6-.6c.4-.5 1-.6 1.5-.3l2 1.1c.6.3.8 1 .5 1.5-.7 1.3-2 1.9-3.4 1.4-3.1-1.1-5.4-3.5-6.4-6.6-.4-1.4.1-2.6 1.2-3.300z" fill="#85acd3"/></svg>
        (555) 014-7200
      </div>
      <div class="sep abs" style="left:316px;"></div>
      <div class="address abs">
        <svg width="15" height="15" viewBox="0 0 15 15" style="margin-top:2px;"><circle cx="7.5" cy="7.5" r="7.5" fill="#e9eef6"/><path d="M7.5 3.2a2.6 2.6 0 0 1 2.6 2.6c0 1.9-2.6 5-2.6 5s-2.6-3.1-2.6-5a2.6 2.6 0 0 1 2.6-2.6z" fill="#85acd3"/><circle cx="7.5" cy="5.8" r="0.9" fill="#e9eef6"/></svg>
        <div>2400 Harbor Ln.,<br>Ste 310 Lakeview,<br>TX 70000</div>
      </div>
      <div class="sep abs" style="left:575px;"></div>
      <div class="contact-extra abs">
        <div>Fax: 555-014-7201</div>
        <div class="web">
          <svg width="12" height="12" viewBox="0 0 12 12"><circle cx="6" cy="6" r="5.2" fill="none" stroke="#e9eef6" stroke-width="1.2"/><ellipse cx="6" cy="6" rx="2.2" ry="5.2" fill="none" stroke="#e9eef6" stroke-width="1"/><line x1="0.8" y1="6" x2="11.2" y2="6" stroke="#e9eef6" stroke-width="1"/></svg>
          www.sbadvisors.com
        </div>
      </div>
    </footer>

    <p class="disclaimer abs">*Senior Bridge Advisors is a private financial services company and not part of the QN. Benefit is determined by the QN based on eligibility.</p>
  </main>
</body>
</html>
```